Brindle Wealth Management Flow Charts

I need help creating three flow charts for my businesses website. We want them to be simple but look professional. This is for a Wealth Management firm. I will attach a word document that has all of the descriptions for everything so you know what icons to use. We just want the chart to have an icon, the names of each step and the corresponding numbers. I will also include some examples of charts we liked as well. Once the winner is selected, we will need help with additional graphic design elements for our website ASAP.
Other font styles liked:
- Goudy Roman

```html
<!DOCTYPE html>
<html lang="en">
<head>
<meta charset="utf-8">
<title>Brindle Wealth Management Flow Charts</title>
<link href="https://fonts.googleapis.com/css2?family=Open+Sans:wght@400&display=swap" rel="stylesheet">
<style>
  :root {
    --teal: #4db6ac;
    --slate: #6b90bd;
    --amber: #fdb44e;
    --navy: #1f4f9b;
    --green: #2eb56f;
    --coral: #f06a47;
    --ink: #333333;
    --paper: #ffffff;
  }
  html, body { margin: 0; padding: 0; overflow: hidden; background: var(--paper); }
  .canvas { width: 1200px; height: 975px; display: block; }
  .chart-title { font-family: "Open Sans", sans-serif; font-size: 32px; fill: var(--ink); text-anchor: middle; }
  .step-number { font-family: "Open Sans", sans-serif; font-size: 62px; fill: var(--ink); }
  .step-label { font-family: "Open Sans", sans-serif; font-size: 28px; fill: var(--paper); }
  .band-teal { fill: var(--teal); }
  .band-slate { fill: var(--slate); }
  .band-amber { fill: var(--amber); }
  .band-navy { fill: var(--navy); }
  .band-green { fill: var(--green); }
  .band-coral { fill: var(--coral); }
  .icon { fill: var(--paper); }
  .icon-line { fill: none; stroke: var(--paper); stroke-width: 7; stroke-linecap: round; stroke-linejoin: round; }
</style>
</head>
<body>
<svg class="canvas" viewBox="0 0 1600 1300" xmlns="http://www.w3.org/2000/svg">
  <defs>
    <polygon id="ribbon-band" points="0,0 52,51 284,51 342,109 342,254 284,196 52,196 0,145"/>
  </defs>

  <!-- Retirement planning -->
  <g class="chart chart-retirement">
    <text class="chart-title" x="307" y="116">The Retirement</text>
    <text class="chart-title" x="307" y="159">Planning</text>
    <text class="chart-title" x="307" y="202">Process</text>
    <use href="#ribbon-band" x="136" y="187" class="band-teal"/>
    <use href="#ribbon-band" x="136" y="351" class="band-slate"/>
    <use href="#ribbon-band" x="136" y="515" class="band-amber"/>
    <use href="#ribbon-band" x="136" y="679" class="band-navy"/>
    <use href="#ribbon-band" x="136" y="843" class="band-green"/>
    <use href="#ribbon-band" x="136" y="1007" class="band-coral"/>

    <text class="step-number" x="142" y="310">1</text>
    <text class="step-label" x="202" y="288">Discovery</text>
    <text class="step-label" x="202" y="326">Meeting</text>
    <g class="icon">
      <circle cx="412" cy="282" r="14"/><path d="M386,316 a26,22 0 0 1 52,0 z"/>
      <circle cx="367" cy="305" r="14"/><path d="M341,338 a26,22 0 0 1 52,0 z"/>
      <circle cx="412" cy="328" r="14"/><path d="M386,362 a26,22 0 0 1 52,0 z"/>
    </g>

    <text class="step-number" x="142" y="466">2</text>
    <text class="step-label" x="202" y="450">Learning</text>
    <g>
      <rect class="icon" x="353" y="430" width="75" height="88"/>
      <g stroke="var(--slate)" stroke-width="4">
        <line x1="362" y1="447" x2="419" y2="447"/><line x1="362" y1="462" x2="419" y2="462"/>
        <line x1="362" y1="477" x2="419" y2="477"/><line x1="362" y1="492" x2="419" y2="492"/>
        <line x1="362" y1="506" x2="419" y2="506"/>
      </g>
    </g>

    <text class="step-number" x="142" y="630">3</text>
    <text class="step-label" x="202" y="614">Planning</text>
    <g class="icon">
      <path d="M390,593 v45 h45 a45,45 0 1 1 -45,-45 z"/>
      <path d="M400,590 a45,45 0 0 1 38,38 h-38 z"/>
    </g>

    <text class="step-number" x="142" y="796">4</text>
    <text class="step-label" x="202" y="782">Execution</text>
    <g class="icon-line">
      <circle cx="410" cy="800" r="30" stroke-width="12"/>
      <circle cx="410" cy="800" r="41" stroke-width="12" stroke-dasharray="12 10" stroke-linecap="butt"/>
      <circle cx="335" cy="828" r="18" stroke-width="8"/>
      <circle cx="335" cy="828" r="25" stroke-width="8" stroke-dasharray="8 7" stroke-linecap="butt"/>
    </g>

    <text class="step-number" x="142" y="962">5</text>
    <text class="step-label" x="204" y="942">Alignment</text>
    <g class="icon">
      <rect x="345" y="950" width="80" height="11" rx="5"/><polygon points="425,938 450,956 425,974"/>
      <rect x="345" y="988" width="80" height="11" rx="5"/><polygon points="345,974 320,993 345,1012"/>
    </g>

    <text class="step-number" x="142" y="1122">6</text>
    <text class="step-label" x="202" y="1108">Review</text>
    <g class="icon-line">
      <circle cx="390" cy="1118" r="31" stroke-width="9"/>
      <line x1="414" y1="1143" x2="450" y2="1180" stroke-width="13"/>
      <path d="M372,1105 a22,22 0 0 1 30,-8" stroke-width="5"/>
    </g>
  </g>

  <!-- Investment management -->
  <g class="chart chart-investment">
    <text class="chart-title" x="810" y="116">Comprehensive</text>
    <text class="chart-title" x="810" y="159">Investment</text>
    <text class="chart-title" x="810" y="202">Management</text>
    <use href="#ribbon-band" x="639" y="187" class="band-teal"/>
    <use href="#ribbon-band" x="639" y="351" class="band-slate"/>
    <use href="#ribbon-band" x="639" y="515" class="band-amber"/>
    <use href="#ribbon-band" x="639" y="679" class="band-navy"/>
    <use href="#ribbon-band" x="639" y="843" class="band-green"/>
    <use href="#ribbon-band" x="639" y="1007" class="band-coral"/>

    <text class="step-number" x="645" y="310">1</text>
    <text class="step-label" x="713" y="281">Understanding</text>
    <text class="step-label" x="713" y="319">your Risk</text>
    <text class="step-label" x="713" y="357">Tolerance</text>
    <g class="icon-line">
      <circle cx="921" cy="332" r="42"/>
      <path d="M903,314 l36,36 M939,314 l-36,36" stroke-width="9"/>
    </g>

    <text class="step-number" x="645" y="466">2</text>
    <text class="step-label" x="713" y="450">Investment</text>
    <text class="step-label" x="713" y="488">Selection</text>
    <g class="icon-line">
      <circle cx="911" cy="487" r="42"/>
      <path d="M890,488 l14,15 l27,-30" stroke-width="9"/>
    </g>

    <text class="step-number" x="645" y="630">3</text>
    <text class="step-label" x="713" y="613">Asset</text>
    <text class="step-label" x="713" y="651">Allocation</text>
    <g>
      <path class="icon" d="M907,688 L882,640 a30,30 0 1 1 50,0 z"/>
      <text x="907" y="643" text-anchor="middle" font-family="Open Sans, sans-serif" font-size="42" fill="var(--amber)">$</text>
    </g>

    <text class="step-number" x="645" y="796">4</text>
    <text class="step-label" x="713" y="783">Tax</text>
    <text class="step-label" x="713" y="821">Efficiency</text>
    <g>
      <path class="icon-line" d="M868,820 a35,35 0 0 1 52,-48 M928,785 a35,35 0 0 1 -52,48" stroke-width="9"/>
      <polygon class="icon" points="910,762 938,762 932,790"/>
      <polygon class="icon" points="886,844 858,844 864,816"/>
    </g>

    <text class="step-number" x="645" y="962">5</text>
    <text class="step-label" x="713" y="944">Distribution</text>
    <text class="step-label" x="713" y="983">Strategy</text>
    <g class="icon">
      <rect x="862" y="976" width="12" height="40"/><rect x="885" y="946" width="12" height="70"/>
      <rect x="908" y="960" width="12" height="56"/><rect x="930" y="937" width="12" height="79"/>
      <rect x="842" y="1016" width="121" height="4"/>
    </g>

    <text class="step-number" x="645" y="1122">6</text>
    <text class="step-label" x="713" y="1099">Behavior</text>
    <text class="step-label" x="713" y="1138">Finance</text>
    <text class="step-label" x="713" y="1176">Coaching</text>
    <g class="icon-line" stroke-width="5">
      <polyline points="866,1094 866,1173 958,1173"/>
      <polyline points="876,1160 892,1118 903,1145 914,1122 926,1150 953,1103"/>
    </g>
  </g>

  <!-- Legacy and estate -->
  <g class="chart chart-legacy">
    <text class="chart-title" x="1300" y="116">Legacy and Estate</text>
    <text class="chart-title" x="1300" y="159">Planning</text>
    <use href="#ribbon-band" x="1129" y="187" class="band-teal"/>
    <use href="#ribbon-band" x="1129" y="351" class="band-slate"/>
    <use href="#ribbon-band" x="1129" y="515" class="band-amber"/>
    <use href="#ribbon-band" x="1129" y="679" class="band-navy"/>
    <use href="#ribbon-band" x="1129" y="843" class="band-green"/>

    <text class="step-number" x="1135" y="310">1</text>
    <text class="step-label" x="1196" y="292">Beneficiaries</text>
    <g class="icon">
      <circle cx="1401" cy="312" r="22"/>
      <path d="M1358,366 a43,36 0 0 1 86,0 z"/>
    </g>

    <text class="step-number" x="1135" y="466">2</text>
    <text class="step-label" x="1198" y="453">Trusts</text>
    <g class="icon">
      <polygon points="1388,436 1432,458 1344,458"/>
      <rect x="1346" y="461" width="84" height="6"/>
      <rect x="1352" y="471" width="8" height="38"/><rect x="1367" y="471" width="8" height="38"/>
      <rect x="1383" y="471" width="8" height="38"/><rect x="1399" y="471" width="8" height="38"/>
      <rect x="1415" y="471" width="8" height="38"/>
      <rect x="1344" y="513" width="88" height="9"/>
    </g>

    <text class="step-number" x="1135" y="630">3</text>
    <text class="step-label" x="1198" y="606">Estate Taxes</text>
    <text class="step-label" x="1198" y="644">and</text>
    <text class="step-label" x="1198" y="682">Assessment</text>
    <g>
      <rect class="icon-line" x="1376" y="615" width="60" height="80" stroke-width="4"/>
      <rect class="icon-line" x="1383" y="622" width="46" height="66" stroke-width="3"/>
      <text x="1406" y="675" text-anchor="middle" font-family="Open Sans, sans-serif" font-size="58" fill="var(--paper)">$</text>
    </g>

    <text class="step-number" x="1135" y="796">4</text>
    <text class="step-label" x="1198" y="779">Annual</text>
    <text class="step-label" x="1198" y="817">Giving</text>
    <g>
      <path class="icon" d="M1340,780 q30,-18 60,-12 l42,22 q6,8 -4,12 l-38,-16 l-16,8 h-30 q-14,0 -14,-14 z"/>
      <circle class="icon" cx="1419" cy="831" r="22"/>
      <text x="1419" y="843" text-anchor="middle" font-family="Open Sans, sans-serif" font-size="30" fill="var(--navy)">$</text>
    </g>

    <text class="step-number" x="1135" y="962">5</text>
    <text class="step-label" x="1197" y="936">Donations and</text>
    <text class="step-label" x="1197" y="975">Charity</text>
    <path class="icon" d="M1406,1012 C1370,990 1360,972 1366,960 C1374,944 1396,944 1406,960 C1416,944 1438,944 1446,960 C1452,972 1442,990 1406,1012 z"/>
  </g>
</svg>
</body>
</html>
```